Bright Sprouts Business Card

speech therapy business card that is fun and professional using my logo.

Wow wonderful dedigns ... 

Industry/Entity Type

Business

Contact Information for Business Card

Rosa Vantrell
Corvid Certified Practising Speech Pathologist
B.Sp.Path MRTQB CRTP
ph: 0419364720
brightsprotsspeechpathology@mailtrove.example
www.brightsproutsspeechpathology.example

```html
<!DOCTYPE html>
<html lang="en">
<head>
<meta charset="utf-8">
<title>Bright Sprouts Speech Pathology – Business Card Backs</title>
<link rel="stylesheet" href="https://fonts.googleapis.com/css2?family=PT+Sans:wght@400;700&family=Michroma&display=swap">
<style>
  :root {
    --stage: #2b2b2b;
    --card-blue: #6bbbe8;
    --band-blue: #4d9fd3;
    --title-band: #eef6fb;
    --title-ink: #4f8fbf;
    --white: #ffffff;
    --brand-ink: #2f6fa8;
    --brand-dot: #6a2a77;
    --social-badge: #3b5590;
    --link-ink: #203a66;
  }
  * { margin: 0; padding: 0; box-sizing: border-box; }
  html, body { width: 960px; height: 1200px; overflow: hidden; background: var(--stage); }
  body { position: relative; font-family: "PT Sans", sans-serif; }

  .card {
    position: absolute; left: 178px; width: 592px; height: 330px;
    background: var(--card-blue); overflow: hidden;
    box-shadow: 0 4px 14px rgba(0,0,0,.45);
  }
  .card--one { top: 61px; }
  .card--two { top: 436px; }
  .card--three { top: 807px; }

  .glow { position: absolute; inset: 0; pointer-events: none; }

  .brand { position: absolute; text-align: center; width: 260px; }
  .brand__dot {
    display: block; margin: 0 auto 10px; width: 62px; height: 62px;
    border-radius: 50%; background: var(--brand-dot);
  }
  .brand__name {
    color: var(--brand-ink); font-weight: 700; font-size: 27px; line-height: 30px;
  }
  .card--one .brand { left: 4px; top: 110px; }
  .card--two .brand { left: 17px; top: 12px; }
  .card--three .brand { left: 15px; top: 90px; }

  .person { position: absolute; left: 353px; top: 146px; right: 0; }
  .person__name {
    color: var(--white); font-weight: 400; font-size: 27px; line-height: 30px; letter-spacing: -0.3px;
  }
  .person__title {
    height: 15px; background: var(--title-band);
    color: var(--title-ink); font-family: "Michroma", sans-serif;
    font-size: 5px; letter-spacing: 0.4px; line-height: 15px; padding-left: 5px;
    white-space: nowrap; overflow: hidden;
  }
  .person__creds {
    text-align: right; padding-right: 6px; margin-top: 5px;
    color: var(--white); font-size: 11.5px;
  }

  .contact { position: absolute; left: 334px; top: 234px; width: 258px; height: 55px; }
  .contact__band { position: absolute; inset: 0; }
  .contact__text {
    position: relative; padding: 10px 0 0 24px;
    color: var(--white); font-size: 10px; line-height: 21px; white-space: nowrap;
  }
  .contact__text b { font-weight: 700; }

  .social { position: absolute; left: 10px; top: 307px; display: flex; align-items: center; gap: 7px; }
  .social__badge {
    width: 46px; height: 16px; background: var(--social-badge); border-radius: 2px;
  }
  .social__link { color: var(--link-ink); font-weight: 700; font-size: 10.5px; }
  .social__name { color: var(--white); font-weight: 700; font-size: 8.5px; margin-left: -50px; width: 44px; text-align: center; }

  .view-label {
    position: absolute; left: 834px; top: 586px;
    color: var(--white); font-size: 26px; letter-spacing: -0.5px;
  }
</style>
</head>
<body>

  <section class="card card--one">
    <svg class="glow" width="592" height="330" viewBox="0 0 592 330" aria-hidden="true">
      <defs>
        <radialGradient id="glowOne" cx="134" cy="180" r="170" gradientUnits="userSpaceOnUse">
          <stop offset="0" stop-color="#ffffff" stop-opacity=".85"/>
          <stop offset=".25" stop-color="#ffffff" stop-opacity=".25"/>
          <stop offset="1" stop-color="#ffffff" stop-opacity="0"/>
        </radialGradient>
      </defs>
      <rect width="592" height="330" fill="url(#glowOne)"/>
      <g fill="#ffffff" fill-opacity=".12" stroke="#ffffff" stroke-opacity=".3">
        <circle cx="-40" cy="70" r="75"/>
        <circle cx="36" cy="172" r="31"/>
        <circle cx="-10" cy="140" r="22"/>
        <circle cx="120" cy="370" r="120" fill-opacity=".05"/>
      </g>
    </svg>
    <div class="brand">
      <span class="brand__dot"></span>
      <p class="brand__name">Bright Sprouts<br>Speech Pathology</p>
    </div>
    <div class="person">
      <h2 class="person__name">Rosa Vantrell</h2>
      <p class="person__title">CORVID CERTIFIED PRACTISING SPEECH PATHOLOGIST</p>
      <p class="person__creds">B.Sp.Path MRTQB CRTP</p>
    </div>
    <div class="contact">
      <svg class="contact__band" width="258" height="55" aria-hidden="true"><polygon points="11,0 258,0 258,55 0,55" fill="var(--band-blue)"/></svg>
      <p class="contact__text"><b>ph:</b> 0419364720<br>brightsprotsspeechpathology@mailtrove.example</p>
    </div>
    <div class="social">
      <span class="social__badge"></span><span class="social__name">chatterpage</span>
      <span class="social__link">chatterpage.example/BrightSproutsSpeechPathology</span>
    </div>
  </section>

  <section class="card card--two">
    <svg class="glow" width="592" height="330" viewBox="0 0 592 330" aria-hidden="true">
      <defs>
        <radialGradient id="glowTwo" cx="150" cy="175" r="160" gradientUnits="userSpaceOnUse">
          <stop offset="0" stop-color="#ffffff" stop-opacity=".8"/>
          <stop offset=".3" stop-color="#ffffff" stop-opacity=".2"/>
          <stop offset="1" stop-color="#ffffff" stop-opacity="0"/>
        </radialGradient>
      </defs>
      <rect width="592" height="330" fill="url(#glowTwo)"/>
      <g fill="#ffffff" fill-opacity=".12" stroke="#ffffff" stroke-opacity=".3">
        <circle cx="-30" cy="40" r="65"/>
        <circle cx="150" cy="178" r="43"/>
        <circle cx="40" cy="172" r="30"/>
        <circle cx="56" cy="255" r="38"/>
        <circle cx="85" cy="270" r="30"/>
        <circle cx="100" cy="220" r="150" fill-opacity=".04"/>
      </g>
    </svg>
    <div class="brand">
      <span class="brand__dot"></span>
      <p class="brand__name">Bright Sprouts<br>Speech Pathology</p>
    </div>
    <div class="person">
      <h2 class="person__name">Rosa Vantrell</h2>
      <p class="person__title">CORVID CERTIFIED PRACTISING SPEECH PATHOLOGIST</p>
      <p class="person__creds">B.Sp.Path MRTQB CRTP</p>
    </div>
    <div class="contact">
      <svg class="contact__band" width="258" height="55" aria-hidden="true"><polygon points="11,0 258,0 258,55 0,55" fill="var(--band-blue)"/></svg>
      <p class="contact__text"><b>ph:</b> 0419364720<br>brightsprotsspeechpathology@mailtrove.example</p>
    </div>
    <div class="social">
      <span class="social__badge"></span><span class="social__name">chatterpage</span>
      <span class="social__link">chatterpage.example/BrightSproutsSpeechPathology</span>
    </div>
  </section>

  <section class="card card--three">
    <div class="brand">
      <span class="brand__dot"></span>
      <p class="brand__name">Bright Sprouts<br>Speech Pathology</p>
    </div>
    <div class="person">
      <h2 class="person__name">Rosa Vantrell</h2>
      <p class="person__title">CORVID CERTIFIED PRACTISING SPEECH PATHOLOGIST</p>
      <p class="person__creds">B.Sp.Path MRTQB CRTP</p>
    </div>
    <div class="contact">
      <svg class="contact__band" width="258" height="55" aria-hidden="true"><polygon points="11,0 258,0 258,55 0,55" fill="var(--band-blue)"/></svg>
      <p class="contact__text"><b>ph:</b> 0419364720<br>brightsprotsspeechpathology@mailtrove.example</p>
    </div>
    <div class="social">
      <span class="social__badge"></span><span class="social__name">chatterpage</span>
      <span class="social__link">chatterpage.example/BrightSproutsSpeechPathology</span>
    </div>
  </section>

  <p class="view-label">3xBack</p>

</body>
</html>
```